TARPLOAD business card design

TARPLOAD is a manufacturer of skip bags supplying both the domestic and commercial market. We wish to convey core characteristics of strength, professionalism and reliability to our customers. We are after a business card that uses our company colours of black and yellow as well as incorporating our logo. Our customers are predominantly in the construction or hardware industry. It is important the cards are professional as we are a small company wishing to appear larger than we actually are. more info on the company and product available at www.tarpload-example.com.au

Target Market(s)

hardware buyers, contruction company owners

Industry/Entity Type

Construction

Requirements
Must have
• company colours of black and yellow - No other colours or variation of yellow black. our company logo. card design must convey "tough"
• Card design must be landscape
• Details to be included on the card are:
• Name and Tiltle
• Phone number : 1300 41 62 53
• Mobile: 0452 718 903
• Fax: 03 9617 4852
• email: dale.hendry@tarpload-example.com.au
• address: PO Box 517, Kelvindale, VIC,3294
• Text in white when on a black background
Nice to have
• I like the idea of the back of the card being black with lighter circle area in the middle with black logo in the centre. Similar to the attached "iconic" card

```html
<!DOCTYPE html>
<html lang="en">
<head>
<meta charset="utf-8">
<title>TARPLOAD Business Card</title>
<link rel="stylesheet" href="https://fonts.googleapis.com/css2?family=Carlito:wght@400;700&display=swap">
<style>
  :root {
    --page: #ffffff;
    --ink: #000000;
    --yellow: #ffcc5c;
    --gold-dark: #5a4520;
    --gold-light: #c9a460;
    --card-back: #191919;
    --disc: #1c1510;
    --glow: #d8c232;
    --faint: #e9e9e9;
    --icon-dark: #2a2622;
  }
  html, body {
    margin: 0;
    padding: 0;
    width: 927px;
    height: 1200px;
    overflow: hidden;
    background: var(--page);
    font-family: "Carlito", "Calibri", sans-serif;
  }
  .sheet { position: relative; width: 927px; height: 1200px; }

  .card-front {
    position: absolute;
    left: 90px; top: 143px;
    width: 740px; height: 415px;
    border: 1px solid var(--ink);
    background: var(--page);
    overflow: hidden;
  }
  .brand-faint {
    position: absolute;
    left: 52px; top: 224px;
    font-weight: 700;
    font-size: 34px;
    letter-spacing: 1px;
    color: var(--faint);
    line-height: 1;
  }
  .brand-faint-mark {
    position: absolute;
    left: 52px; top: 186px;
    width: 30px; height: 30px;
    background: var(--faint);
  }
  .holder-name {
    position: absolute;
    right: 22px; top: 42px;
    margin: 0;
    font-weight: 400;
    font-size: 45px;
    line-height: 1;
    color: var(--yellow);
  }
  .holder-title {
    position: absolute;
    right: 20px; top: 102px;
    margin: 0;
    font-size: 23px;
    line-height: 1;
    color: var(--ink);
  }
  .contact-list {
    position: absolute;
    left: 326px; top: 234px;
    margin: 0; padding: 0;
    list-style: none;
  }
  .contact-list li {
    display: flex;
    align-items: center;
    height: 21px;
    font-size: 19.5px;
    color: var(--ink);
    white-space: nowrap;
  }
  .contact-icon {
    width: 38px; height: 21px;
    margin-right: 2px;
    flex: none;
  }
  .band-solid {
    position: absolute;
    left: 2px; bottom: 0;
    width: 258px; height: 29px;
    background: var(--ink);
  }
  .band-texture {
    position: absolute;
    left: 266px; bottom: 0;
    width: 474px; height: 29px;
    background: linear-gradient(180deg, var(--gold-dark), var(--gold-light) 50%, var(--gold-dark));
  }

  .card-back {
    position: absolute;
    left: 91px; top: 604px;
    width: 740px; height: 415px;
    background: var(--card-back);
  }
  .back-disc {
    position: absolute;
    left: 228px; top: 75px;
    width: 314px; height: 240px;
    border-radius: 50%;
    background: var(--disc);
    box-shadow: 0 0 0 3px var(--glow), 0 0 10px 5px rgba(216,194,50,0.55);
  }
  .back-brand {
    position: absolute;
    left: 0; right: 0; top: 98px;
    text-align: center;
    font-weight: 700;
    font-size: 42px;
    line-height: 1;
    color: var(--ink);
  }
</style>
</head>
<body>
<div class="sheet">
  <section class="card-front">
    <div class="brand-faint-mark"></div>
    <div class="brand-faint">TARPLOAD</div>
    <h1 class="holder-name">Dale Hendry</h1>
    <p class="holder-title">Managing Director</p>
    <ul class="contact-list">
      <li>
        <svg class="contact-icon" viewBox="0 0 38 21"><ellipse cx="19" cy="10.5" rx="18" ry="10" fill="var(--icon-dark)"/><rect x="11" y="7" width="16" height="7" fill="none" stroke="var(--yellow)" stroke-width="1.2"/></svg>
        PO Box 517, Kelvindale, VIC,3294
      </li>
      <li>
        <svg class="contact-icon" viewBox="0 0 38 21"><ellipse cx="19" cy="10.5" rx="18" ry="10" fill="var(--icon-dark)"/><path d="M11 9 Q19 3 27 9 L25 11 L13 11 Z M14 11 L24 11 L25 16 L13 16 Z" fill="var(--yellow)"/></svg>
        1300 41 62 53
      </li>
      <li>
        <svg class="contact-icon" viewBox="0 0 38 21"><ellipse cx="19" cy="10.5" rx="18" ry="10" fill="var(--icon-dark)"/><rect x="15" y="4" width="8" height="13" rx="1.5" fill="var(--yellow)"/></svg>
        0452 718 903
      </li>
      <li>
        <svg class="contact-icon" viewBox="0 0 38 21"><ellipse cx="19" cy="10.5" rx="18" ry="10" fill="var(--icon-dark)"/><rect x="12" y="9" width="14" height="6" fill="var(--yellow)"/><rect x="14" y="5" width="10" height="4" fill="var(--yellow)" opacity="0.7"/></svg>
        03 9617 4852
      </li>
      <li>
        <svg class="contact-icon" viewBox="0 0 38 21"><ellipse cx="19" cy="10.5" rx="18" ry="10" fill="var(--icon-dark)"/><rect x="12" y="6" width="14" height="9" fill="none" stroke="var(--yellow)" stroke-width="1.2"/><path d="M12 6 L19 11 L26 6" fill="none" stroke="var(--yellow)" stroke-width="1.2"/></svg>
        dale.hendry@tarpload-example.com.au
      </li>
    </ul>
    <div class="band-solid"></div>
    <div class="band-texture" role="img" aria-label="Gold corrugated texture strip"></div>
  </section>

  <section class="card-back">
    <div class="back-disc">
      <div class="back-brand">TARPLOAD</div>
    </div>
  </section>
</div>
</body>
</html>
```